Web Design Project

Psychotherapy and Counselling Practice needs a landing page web design.

My business "Larkspur Advisory" specialises in the treatment of Anxiety and Depression with a holistic approach, endeavouring to unlock the key that holds us to ransom in a life that is imbalanced, frustrating, and ultimately of our own making due to our own perceptions and behaviours.

There is much that impacts us which we cannot change, but we are always in control of how we think, and how we frame our experiences.....learning to challenge those thoughts and behaviours that are destructive and disempowering opens up a world of joyful possibility. Life is about making choices, learn to make wiser and healthier choices.......

Larkspur Advisory has a client base of individual clients but will seek to expand to offer services to the Corporate world by offering an adjunct to employers for established "Wellness Programs".

Larkspur Advisory is a highly professional, ethically bound business, with the needs of the client at the forefront of all we do.

Larkspur Advisory wishes to avoid the usual "jargon driven" psychobabble offered on many counselling web pages. It aims to be stylishly presented, clean in look and with as few "words" as possible and a largely white background (faster loading and more powerful impact of what is stated), those words contained in the webpage should be meaningful, persuasive and have an impact simply at glance. Larkspur does not want , or expect, those prospective clients in need of support , to be reading through volumes of industry driven cliches.

At this point Larkspur is just looking for a high quality landing page. However in time this will likely expand to include other sections such as case studies, video content etc.

Target Market(s)

Those in need of emotional support, suffering mental health issues, and those simply wanting to become self aware supported by a mindful therapist.

Industry/Entity Type

Industry

Requirements
Must have
• The design must incorporate the Larkspur logo and colour schemes found on the attached files.

```html
<!DOCTYPE html>
<html lang="en">
<head>
<meta charset="utf-8">
<title>Larkspur Advisory</title>
<link href="https://fonts.googleapis.com/css2?family=Carlito:wght@400;700&display=swap" rel="stylesheet">
<style>
:root{
  --green:#8ab20f;
  --green-dark:#6f9300;
  --heading-green:#5f7f0a;
  --grey:#6f6f6f;
  --text:#3c3c3c;
  --white:#ffffff;
}
*{box-sizing:border-box;margin:0;padding:0}
html,body{width:1200px;height:1164px;overflow:hidden;background:var(--white)}
body{position:relative;font-family:"Carlito",Calibri,sans-serif;color:var(--text)}
.abs{position:absolute}
.top-rule{left:0;top:0;width:1200px;height:3px;background:var(--green)}
.brand{left:150px;top:58px;font-size:24px;letter-spacing:1px;color:var(--green)}
.search{left:763px;top:25px;width:169px;height:28px;border:1px solid #c8c8c8;background:#fff;font-size:11px;color:#555;padding:7px 10px}
.search svg{position:absolute;right:7px;top:6px}
.social{top:25px;width:26px;height:26px;border-radius:50%}
.s1{left:950px;background:#2e5fa8}.s2{left:985px;background:#4fb3e0}.s3{left:1020px;background:#e8782a}
.call{left:793px;top:74px;display:flex;align-items:center;gap:8px}
.call-icon{width:34px;height:34px;border-radius:50%;background:linear-gradient(#f4f4f4,#cfcfcf);display:flex;align-items:center;justify-content:center}
.call-label{font-size:16px;color:#666}
.call-number{font-size:22px;color:var(--green-dark)}
.nav{left:0;top:134px;width:1200px;height:56px}
.nav ul{list-style:none}
.nav li{position:absolute;top:28px;transform:translateX(-50%);font-size:12.5px;color:#fff;font-weight:700;letter-spacing:.2px}
.nav .div{position:absolute;top:0;width:1px;height:56px;background:#5c5c5c}
.hero{left:0;top:189px;width:1200px;height:344px;overflow:hidden;background:linear-gradient(90deg,#e4e4e4 0%,#f7f7f7 30%,#f2f2f2 70%,#e0e0e0 100%)}
.hero-shadow{left:0;top:531px;width:640px;height:14px;background:radial-gradient(ellipse at 60% 0,rgba(0,0,0,.55),rgba(0,0,0,0) 70%)}
.hero-figure{position:absolute;left:600px;top:18px;width:340px;height:326px;background:radial-gradient(ellipse 50% 55% at 50% 55%,#c4c1ba 0%,#a9a69f 45%,rgba(240,240,240,0) 100%)}
.hero-title{left:251px;top:225px;width:440px;font-weight:400;font-size:36px;line-height:37px;color:var(--heading-green)}
.hero-copy{left:252px;top:312px;width:370px;font-size:13px;line-height:18.5px;color:#333}
.btn{background:var(--green);color:#2c3a00;font-size:12px;border-radius:2px}
.read-more{left:257px;top:399px;width:73px;height:32px;display:flex;align-items:center;justify-content:center;font-size:11.5px}
.dot{top:476px;width:16px;height:16px;border-radius:50%;background:#b5b5b5}
.dot.on{background:var(--green)}
.arrow{top:348px;width:41px;height:41px;border-radius:50%;background:#999;display:flex;align-items:center;justify-content:center}
.card{top:631px;width:214px;height:376px}
.card-body{position:absolute;left:0;top:6px;width:214px;height:364px;background:var(--grey);padding:28px 12px 0 12px;color:#fff}
.card h2{font-weight:400;font-size:18px;margin-bottom:10px}
.card-img{width:190px;height:106px;border:2px solid #a9a9a9;margin-bottom:18px}
.card p{font-size:12px;line-height:16.6px;text-align:justify;margin-bottom:12px}
.card .more{position:absolute;left:12px;top:322px;width:48px;height:20px;display:flex;align-items:center;justify-content:center;font-size:12px}
.card svg{position:absolute;left:0}
.footer{left:0;top:1029px;width:1200px;height:135px;background:linear-gradient(#e6e6e6,#f6f6f6);border-top:2px solid #d4d4d4}
.f-contact{left:152px;display:flex;align-items:center;gap:12px;font-size:14px;color:#222}
.f-links{right:154px;top:1057px;font-size:11.5px;color:#222;text-align:right}
.f-copy{right:154px;top:1079px;font-size:11.5px;color:#222}
.f-rule{left:152px;top:1122px;width:894px;height:1px;background:#c4c4c4}
.f-social{top:1136px;width:16px;height:16px;border-radius:2px}
</style>
</head>
<body>
<div class="abs top-rule"></div>
<div class="abs brand">LARKSPUR</div>

<div class="abs search">Search
  <svg width="14" height="14" viewBox="0 0 14 14"><circle cx="5.5" cy="5.5" r="3.8" fill="none" stroke="#555" stroke-width="1.6"/><line x1="8.4" y1="8.4" x2="12.5" y2="12.5" stroke="#555" stroke-width="2"/></svg>
</div>
<div class="abs social s1"></div><div class="abs social s2"></div><div class="abs social s3"></div>

<div class="abs call">
  <div class="call-icon"><svg width="16" height="18" viewBox="0 0 16 18"><path d="M4 1c1 0 2 3 2 4s-2 1-1.5 3 2 4 3.5 5 1.5-1 2.5-1 3 2 3 3-2 2-3 2C6 17 1 10 1 5c0-2 2-4 3-4z" fill="#8a8a8a"/></svg></div>
  <span class="call-label">Call Us Now</span>
  <span class="call-number">0400 218 765</span>
</div>

<svg class="abs" style="left:0;top:100px" width="1200" height="90" viewBox="0 0 1200 90">
  <path d="M0 34 C250 90 500 30 1200 34 L1200 90 L0 90 Z" fill="#6f6f6f"/>
  <path d="M0 14 C150 50 300 60 500 48 C650 38 720 28 800 25 C600 30 480 48 320 52 C180 55 80 40 0 24 Z" fill="#8ab20f"/>
</svg>
<nav class="abs nav">
  <ul>
    <li style="left:213px">HOME</li>
    <li style="left:345px">ABOUT US</li>
    <li style="left:462px">SERVICES</li>
    <li style="left:572px;top:26px">CONSULTING</li>
    <li style="left:663px;top:26px">FAQ'S</li>
    <li style="left:757px;top:26px">CONTACT US</li>
  </ul>
  <span class="div" style="left:291px"></span><span class="div" style="left:407px"></span><span class="div" style="left:520px"></span><span class="div" style="left:629px"></span><span class="div" style="left:699px"></span>
</nav>

<section class="abs hero">
  <div class="hero-figure" role="img" aria-label="Silver sculpture of a seated figure with head bowed"></div>
</section>
<div class="abs hero-shadow"></div>
<h1 class="abs hero-title">Anxiety and Depression<br>approach consulting</h1>
<p class="abs hero-copy">Sometimes we all need support, particularly when we are feeling depressed, , anxious or confused about our current life situation. Cognitive Behavioral Therapy concentrates on what can be done about these problems TODAY. It is an active directive</p>
<div class="abs btn read-more">READ MORE</div>
<span class="abs dot" style="left:259px"></span><span class="abs dot on" style="left:281px"></span><span class="abs dot" style="left:302px"></span><span class="abs dot" style="left:326px"></span>
<div class="abs arrow" style="left:158px"><svg width="14" height="20" viewBox="0 0 14 20"><path d="M11 2 L3 10 L11 18" fill="none" stroke="#fff" stroke-width="3"/></svg></div>
<div class="abs arrow" style="left:999px"><svg width="14" height="20" viewBox="0 0 14 20"><path d="M3 2 L11 10 L3 18" fill="none" stroke="#fff" stroke-width="3"/></svg></div>

<article class="abs card" style="left:153px">
  <div class="card-body">
    <h2>Consulting Treatment</h2>
    <div class="card-img" role="img" aria-label="Hands fitting puzzle pieces together" style="background:linear-gradient(135deg,#1c1c1c,#c98a6a 50%,#e8e8e8)"></div>
    <p>Stillpoint provides specialist counselling treatment for people experiencing anxiety, panic, stress and depression in a friendly and supportive environment.</p>
    <p>Individual counselling is provided plus group programs for social phobia</p>
    <div class="btn more">MORE</div>
  </div>
  <svg style="top:0" width="214" height="10"><path d="M0 8 C70 0 150 2 214 6" stroke="#8ab20f" stroke-width="3" fill="none"/></svg>
  <svg style="top:364px" width="214" height="12"><path d="M0 2 C70 10 150 10 214 8" stroke="#8ab20f" stroke-width="3" fill="none"/></svg>
</article>

<article class="abs card" style="left:378px">
  <div class="card-body">
    <h2>Consulting Sessions</h2>
    <div class="card-img" role="img" aria-label="Group meeting around a table seen from above" style="background:linear-gradient(135deg,#3a3a3a,#a08a70 50%,#5a5a5a)"></div>
    <p>Each person coming to Stillpoint has unique needs and will have an individually designed program of recovery in easily managed steps.</p>
    <p>Counselling is viewed as a collaborative relationship where opinions and decisions are respected.</p>
    <div class="btn more">MORE</div>
  </div>
  <svg style="top:0" width="214" height="10"><path d="M0 8 C70 0 150 2 214 6" stroke="#8ab20f" stroke-width="3" fill="none"/></svg>
  <svg style="top:364px" width="214" height="12"><path d="M0 2 C70 10 150 10 214 8" stroke="#8ab20f" stroke-width="3" fill="none"/></svg>
</article>

<article class="abs card" style="left:605px">
  <div class="card-body">
    <h2>Anxiety and Depression</h2>
    <div class="card-img" role="img" aria-label="Black and white portrait of a worried young woman" style="background:linear-gradient(135deg,#d8d8d8,#7a7a7a 55%,#2a2a2a)"></div>
    <p>Children and adolescents frequently experience significant problems with anxiety or depression.</p>
    <p>Counselling treatment can help the young person to overcome the distress associated with anxiety or depression and also prevents problems becoming.</p>
    <div class="btn more">MORE</div>
  </div>
  <svg style="top:0" width="214" height="10"><path d="M0 8 C70 0 150 2 214 6" stroke="#8ab20f" stroke-width="3" fill="none"/></svg>
  <svg style="top:364px" width="214" height="12"><path d="M0 2 C70 10 150 10 214 8" stroke="#8ab20f" stroke-width="3" fill="none"/></svg>
</article>

<article class="abs card" style="left:832px">
  <div class="card-body">
    <h2>About Us</h2>
    <div class="card-img" role="img" aria-label="Portrait of a distressed woman holding her face" style="background:linear-gradient(135deg,#1a1a1a,#8a4a35 50%,#1a1a1a)"></div>
    <p>Counsellors at Stillpoint are all qualified psychologists with many years experience in the treatment of anxiety disorders and depression.</p>
    <p style="margin-top:20px">Individual counselling is provided plus group programs for social phobia</p>
    <div class="btn more">MORE</div>
  </div>
  <svg style="top:0" width="214" height="10"><path d="M0 8 C70 0 150 2 214 6" stroke="#8ab20f" stroke-width="3" fill="none"/></svg>
  <svg style="top:364px" width="214" height="12"><path d="M0 2 C70 10 150 10 214 8" stroke="#8ab20f" stroke-width="3" fill="none"/></svg>
</article>

<footer class="abs footer"></footer>
<div class="abs f-contact" style="top:1052px">
  <svg width="16" height="14" viewBox="0 0 16 14"><path d="M1 5 C4 0 12 0 15 5 L12 6 L11 4 H5 L4 6 Z M3 7 H13 L14 13 H2 Z" fill="#666"/></svg>
  <span>0400 218 765</span>
</div>
<div class="abs f-contact" style="top:1079px">
  <svg width="18" height="12" viewBox="0 0 18 12"><rect x="0.5" y="0.5" width="17" height="11" fill="#999"/><path d="M1 1 L9 7 L17 1" stroke="#eee" fill="none"/></svg>
  <span>care@larkspuradvisory.com</span>
</div>
<div class="abs f-links">Home &nbsp;&nbsp;|&nbsp;&nbsp; About Us &nbsp;&nbsp;|&nbsp;&nbsp; Services &nbsp;&nbsp;|&nbsp;&nbsp; Consulting &nbsp;&nbsp;|&nbsp;&nbsp; Testimonials &nbsp;&nbsp;|&nbsp;&nbsp; FAQ's &nbsp;&nbsp;|&nbsp;&nbsp; Contact Us</div>
<div class="abs f-copy">Copyrights @ 2013 All Rights Reserved</div>
<div class="abs f-rule"></div>
<span class="abs f-social" style="left:560px;background:#3b5b98"></span>
<span class="abs f-social" style="left:581px;background:#4fb3e0"></span>
<span class="abs f-social" style="left:602px;background:#1f6fa8"></span>
<span class="abs f-social" style="left:623px;background:#e8782a"></span>
</body>
</html>
```